Estate Planning Law Firm opening new branch in Florida

I am an experienced estate planning attorney that recently relocated to Florida. Looking for a banner Ad to place on platforms such as YardLoop, Chatterly and Pixmora to create publicity for firm and new leads.

```html
<!DOCTYPE html>
<html lang="en">
<head>
<meta charset="UTF-8">
<title>Serelane Law Firm – Estate Planning Banner</title>
<link href="https://fonts.googleapis.com/css2?family=Oswald:wght@600&family=Source+Sans+3:ital,wght@0,600;1,500;1,700&family=Open+Sans:wght@700&family=Montserrat:wght@600&display=swap" rel="stylesheet">
<style>
  :root {
    --backdrop: #e4e4e4;
    --navy: #2c3b50;
    --teal: #1b6e70;
    --gold: #c9932f;
    --white: #ffffff;
    --ring-light: #d3d8de;
    --ring-edge: #eef0f2;
    --photo-light: #b9b9b9;
    --photo-dark: #3a3a3a;
  }
  * { margin: 0; padding: 0; box-sizing: border-box; }
  html, body { width: 1200px; height: 675px; overflow: hidden; background: var(--backdrop); }
  .banner {
    position: absolute; left: 309px; top: 47px;
    width: 581px; height: 581px;
    background: var(--white);
    box-shadow: 0 2px 6px rgba(0,0,0,0.18);
    overflow: hidden;
  }
  .hero-photo {
    position: absolute; left: 0; top: 0; width: 581px; height: 258px;
    background: linear-gradient(160deg, var(--photo-dark) 0%, #6b6b6b 35%, var(--photo-light) 60%, #8a8a8a 80%, var(--photo-dark) 100%);
  }
  .message-panel {
    position: absolute; left: 0; top: 258px; width: 581px; height: 220px;
    background: var(--navy);
  }
  .headline {
    position: absolute; left: 260px; top: 282px;
    font-family: "Oswald", sans-serif; font-weight: 600;
    font-size: 25px; line-height: 29px; color: var(--gold);
    letter-spacing: -0.2px;
  }
  .headline-rule {
    position: absolute; left: 262px; top: 347px; width: 94px; height: 3px;
    background: var(--gold);
  }
  .intro {
    position: absolute; left: 20px; width: 541px;
    font-family: "Source Sans 3", sans-serif; font-style: italic; font-weight: 500;
    font-size: 12.3px; line-height: 15.5px; color: var(--white); text-align: center;
  }
  .intro.first { top: 388px; }
  .intro.second { top: 435px; }
  .brand-badge { position: absolute; left: 15px; top: 142px; width: 224px; height: 224px; }
  .brand-name {
    position: absolute; left: 15px; top: 230px; width: 224px; text-align: center;
    font-family: "Source Sans 3", sans-serif; font-weight: 600; color: var(--navy);
  }
  .brand-name .name { display: block; font-size: 21px; letter-spacing: 0.5px; line-height: 24px; }
  .brand-name .suffix { display: block; font-size: 8px; letter-spacing: 0.6px; line-height: 10px; }
  .cta-band {
    position: absolute; left: 0; top: 478px; width: 581px; height: 65px;
    background: var(--teal);
  }
  .cta-text {
    position: absolute; right: 363px; top: 18px; text-align: right;
    font-family: "Source Sans 3", sans-serif; font-style: italic; font-weight: 700;
    color: var(--white); line-height: 14px;
  }
  .cta-text .small { font-size: 11.5px; display: block; }
  .cta-text .large { font-size: 14px; display: block; }
  .phone-icon { position: absolute; left: 236px; top: 14px; width: 37px; height: 37px; }
  .phone-number {
    position: absolute; left: 276px; top: 13px;
    font-family: "Open Sans", sans-serif; font-weight: 700;
    font-size: 27px; line-height: 38px; color: var(--white);
  }
  .contact-bar {
    position: absolute; left: 0; top: 543px; width: 581px; height: 38px;
    font-family: "Montserrat", sans-serif; font-weight: 600;
    font-size: 12.5px; color: var(--navy); line-height: 38px;
  }
  .contact-bar .email { position: absolute; left: 94px; }
  .contact-bar .website { position: absolute; left: 316px; }
</style>
</head>
<body>
  <div class="banner">
    <div class="hero-photo" role="img" aria-label="Black and white photo of an attorney reading a book at a desk behind brass scales of justice"></div>
    <div class="message-panel"></div>

    <svg class="brand-badge" viewBox="0 0 224 224" aria-hidden="true">
      <circle cx="112" cy="112" r="112" fill="var(--ring-edge)"/>
      <circle cx="112" cy="112" r="106" fill="var(--ring-light)"/>
      <circle cx="112" cy="112" r="96" fill="var(--white)"/>
      <circle cx="112" cy="112" r="92" fill="var(--navy)"/>
      <circle cx="112" cy="112" r="81" fill="var(--white)"/>
    </svg>
    <div class="brand-name">
      <span class="name">SERELANE</span>
      <span class="suffix">LAW FIRM, PLLC</span>
    </div>

    <h1 class="headline">Building Lifetime Relationships<br>Through Trust and Expertise</h1>
    <div class="headline-rule"></div>

    <p class="intro first">As an experienced estate planning attorney, I am dedicated to treating every client not just as a<br>one-time transaction but as a lifelong partner in securing their legacy.</p>
    <p class="intro second">New to Florida, but with years of expertise in estate planning, I am here to support you and your<br>family for generations to come.</p>

    <div class="cta-band">
      <p class="cta-text"><span class="small">Schedule a</span><span class="large">Free Consultation Today!</span></p>
      <svg class="phone-icon" viewBox="0 0 40 40" aria-hidden="true">
        <circle cx="20" cy="20" r="18" fill="none" stroke="var(--white)" stroke-width="2.6"/>
        <path d="M14.2 11.5c.7-.6 1.7-.5 2.2.3l1.9 3c.4.7.3 1.5-.3 2l-1.3 1.1c.9 2 2.5 3.7 4.5 4.6l1.1-1.3c.5-.6 1.4-.7 2-.3l3 1.9c.8.5.9 1.5.3 2.2l-1.4 1.6c-.8.9-2.1 1.2-3.2.8-5-1.9-8.9-5.8-10.8-10.8-.4-1.1-.1-2.4.8-3.2z" fill="var(--white)"/>
      </svg>
      <p class="phone-number">(000) 000-0000</p>
    </div>

    <div class="contact-bar">
      <span class="email">Email: example@email.com</span>
      <span class="website">Website: www.example.com</span>
    </div>
  </div>
</body>
</html>
```